Larkwood Plumbing and Rooter wrap design

I would like to incorporate my logo into the design of the wrap. I would also like "Larkwood Plumbing and Rooter" on the wrap. Pretty open to designs. I would also like the number '555-014-2763" I included a photo of the van I intend to wrap. You have a lot of design room on the van. Maybe try designs with more colors than white. We really want to stand out from the crowd. NOT A LOT OF PINK. I uploaded some photos of wraps that I like for a better idea. I would like to have strong bold lines. I prefer the van wrap style in the included photos that has the Quorvin name on the van (image 1 and 2).

Target Market(s)

Every homeowner, real estate owner, property managers

Colors
78c3e4
f37122
33b8a4
ec1f27
ffc214
fbed22
9ccb3b
0455a3
f78f20

Requirements
Must have
• Design on both the sides and back. Also must have the logo, company name and number (in company description).
Nice to have
• Standout design! something that catches the customers eye. Maybe the background of Los Angeles, California. Nice strong bold colors and lines maybe. Clean looking but not boring. PLEASE USE VERY LITTLE PINK, IF ANY IN THE DESIGN . It's OK to just have the pink in the logo and that's it.

```html
<!DOCTYPE html>
<html lang="en">
<head>
<meta charset="utf-8">
<title>Larkwood Plumbing and Rooter – Truck Wrap</title>
<link rel="stylesheet" href="https://fonts.googleapis.com/css2?family=Cabin:wght@500;600&display=swap">
<style>
  :root {
    --wrap-teal: #1f9c8b;
    --wrap-teal-light: #33b8a4;
    --wrap-blue: #0455a3;
    --wrap-blue-light: #2f8fd6;
    --wrap-navy: #0a3f78;
    --logo-ring: #0455a3;
    --accent-pink: #e4469a;
    --paper: #ffffff;
    --stripe: #f4f4f4;
    --canvas-bg: #eef0f2;
  }
  html, body {
    margin: 0;
    padding: 0;
    width: 793px;
    height: 1200px;
    overflow: hidden;
    background: var(--canvas-bg);
  }
  .wrap-sheet {
    position: relative;
    width: 793px;
    height: 1200px;
    font-family: "Cabin", sans-serif;
  }
  .wrap-panel {
    position: absolute;
    display: block;
  }
  .side-panel { left: 40px; top: 90px; width: 713px; height: 330px; }
  .back-panel { left: 161px; top: 540px; width: 470px; height: 520px; }
  .wrap-text { font-family: "Cabin", sans-serif; font-weight: 600; }
  .ampersand { fill: var(--wrap-navy); }
  .headline { fill: var(--paper); }
  .logo-name { fill: var(--logo-ring); font-weight: 600; }
</style>
</head>
<body>
<main class="wrap-sheet">

  <!-- Side of box -->
  <svg class="wrap-panel side-panel" viewBox="0 0 713 330" aria-label="Side wrap">
    <defs>
      <radialGradient id="side-blue-glow" cx="0.55" cy="0.45" r="0.7">
        <stop offset="0" stop-color="var(--wrap-blue-light)"/>
        <stop offset="1" stop-color="var(--wrap-blue)"/>
      </radialGradient>
      <radialGradient id="side-teal-glow" cx="0.3" cy="0.4" r="0.7">
        <stop offset="0" stop-color="var(--wrap-teal-light)"/>
        <stop offset="1" stop-color="var(--wrap-teal)"/>
      </radialGradient>
    </defs>
    <rect class="teal-field" width="713" height="330" fill="url(#side-teal-glow)"/>
    <path class="divider-stripe" d="M318 0 C222 100 160 220 158 330 L178 330 C182 220 242 100 338 0 Z" fill="var(--stripe)"/>
    <path class="blue-field" d="M338 0 C242 100 182 220 178 330 L713 330 L713 0 Z" fill="url(#side-blue-glow)"/>

    <text class="wrap-text headline" x="24" y="32" font-size="20">555.014.2763</text>
    <circle class="logo-mini" cx="70" cy="80" r="32" fill="var(--paper)" stroke="var(--accent-pink)" stroke-width="2"/>
    <text class="wrap-text logo-name" x="70" y="78" font-size="7" text-anchor="middle">LARKWOOD</text>
    <text class="wrap-text logo-name" x="70" y="88" font-size="6" text-anchor="middle">PLUMBING &amp; ROOTER</text>

    <g class="logo-badge">
      <circle cx="318" cy="156" r="112" fill="var(--paper)" stroke="var(--accent-pink)" stroke-width="4"/>
      <text class="wrap-text logo-name" x="318" y="134" font-size="26" text-anchor="middle">LARKWOOD</text>
      <text class="wrap-text logo-name" x="318" y="166" font-size="22" text-anchor="middle">PLUMBING</text>
      <text class="wrap-text logo-name" x="318" y="196" font-size="18" text-anchor="middle">AND ROOTER</text>
    </g>

    <text class="wrap-text headline" x="692" y="58" font-size="26" text-anchor="end">LARKWOOD PLUMBING</text>
    <text class="wrap-text ampersand" x="612" y="168" font-size="70" text-anchor="middle">&amp;</text>
    <text class="wrap-text headline" x="690" y="238" font-size="40" text-anchor="end">ROOTER</text>
    <text class="wrap-text headline" x="672" y="290" font-size="28" font-style="italic" text-anchor="end">555.014.2763</text>
  </svg>

  <!-- Rear doors -->
  <svg class="wrap-panel back-panel" viewBox="0 0 470 520" aria-label="Rear wrap">
    <defs>
      <radialGradient id="back-blue-glow" cx="0.6" cy="0.4" r="0.7">
        <stop offset="0" stop-color="var(--wrap-blue-light)"/>
        <stop offset="1" stop-color="var(--wrap-blue)"/>
      </radialGradient>
      <radialGradient id="back-teal-glow" cx="0.3" cy="0.5" r="0.7">
        <stop offset="0" stop-color="var(--wrap-teal-light)"/>
        <stop offset="1" stop-color="var(--wrap-teal)"/>
      </radialGradient>
    </defs>
    <rect class="teal-field" width="470" height="520" fill="url(#back-teal-glow)"/>
    <path class="divider-stripe" d="M244 0 C150 70 110 200 150 330 C180 420 230 480 262 520 L276 520 C244 480 196 420 166 330 C128 200 168 72 262 0 Z" fill="var(--stripe)"/>
    <path class="blue-field" d="M262 0 C168 72 128 200 166 330 C196 420 244 480 276 520 L470 520 L470 0 Z" fill="url(#back-blue-glow)"/>

    <text class="wrap-text headline" x="235" y="96" font-size="37" text-anchor="middle">LARKWOOD PLUMBING</text>

    <g class="logo-badge">
      <circle cx="157" cy="290" r="122" fill="var(--paper)" stroke="var(--accent-pink)" stroke-width="4"/>
      <text class="wrap-text logo-name" x="157" y="268" font-size="28" text-anchor="middle">LARKWOOD</text>
      <text class="wrap-text logo-name" x="157" y="302" font-size="24" text-anchor="middle">PLUMBING</text>
      <text class="wrap-text logo-name" x="157" y="334" font-size="19" text-anchor="middle">AND ROOTER</text>
    </g>

    <text class="wrap-text ampersand" x="372" y="262" font-size="80" text-anchor="middle">&amp;</text>
    <text class="wrap-text headline" x="294" y="338" font-size="40">ROOTER</text>
    <text class="wrap-text headline" x="339" y="442" font-size="28" text-anchor="middle" letter-spacing="1">555.014.2763</text>
  </svg>

</main>
</body>
</html>
```